NFC (Near field communication) - Business Card Design

IT/ Telecom:

We would like a new business card that contains our logo, contact info for the company and contact info for the owner. We also wolud like to be innovative, and create NFC technology inside the card.

This means that mobile phones can be placed on the card, and the contactinfo automaticly stores into the phonebook. Therefore, a cirkle or similar - with the text: "Place your phone here!" (please write it in Norwagian): "Aktiver NFC og legg mobilen din her!".

Please google NFC or near field communication and use your imagination on the design as we love surprises :-)

Industry/Entity Type

Communication

Requirements
Must have
• Text: "Activate NFC on your phone and place your mobile here - in Norwegian: "Aktiver NFC og legg mobilen din her!".
Nice to have
• Please see attachment #5 for inspiration.

```html
<!DOCTYPE html>
<html lang="no">
<head>
<meta charset="utf-8">
<title>Netlinka – NFC visittkort</title>
<link href="https://fonts.googleapis.com/css2?family=Lato:wght@400;700&display=swap" rel="stylesheet">
<style>
  :root {
    --backdrop: #1fb0d6;
    --card: #f7f8f9;
    --brand: #4b7a8e;
    --brand-text: #5b8293;
    --ink: #2f3a40;
    --wave: #d3dde3;
    --tagline: #7f9aa7;
  }
  * { margin: 0; padding: 0; box-sizing: border-box; }
  html, body {
    width: 1200px; height: 900px; overflow: hidden;
    background: var(--backdrop);
    font-family: "Lato", sans-serif;
  }
  .stage {
    position: relative; width: 1200px; height: 900px;
    display: flex; align-items: center; justify-content: center; gap: 50px;
  }
  .card {
    position: relative; width: 500px; height: 286px;
    background: var(--card);
    box-shadow: 0 6px 18px rgba(0, 40, 60, 0.25);
  }
  /* NFC side */
  .nfc-zone {
    position: absolute; left: 110px; top: 24px;
    width: 280px; height: 190px; border-radius: 50%;
    background: radial-gradient(ellipse at center, rgba(211, 221, 227, 0.9) 0%, rgba(211, 221, 227, 0.45) 55%, rgba(247, 248, 249, 0) 72%);
  }
  .nfc-brand {
    position: absolute; left: 0; right: 0; top: 104px;
    text-align: center; font-weight: 700; font-size: 26px;
    color: var(--brand); letter-spacing: 0.5px;
  }
  .nfc-tagline {
    position: absolute; left: 0; right: 0; bottom: 34px;
    text-align: center; font-size: 14px; color: var(--tagline);
  }
  /* Contact side */
  .logo {
    position: absolute; top: 30px; right: 34px;
    display: flex; align-items: center; gap: 12px;
  }
  .logo-square { width: 46px; height: 34px; background: var(--brand); border-radius: 4px; }
  .logo-name { font-size: 38px; font-weight: 400; color: var(--brand-text); letter-spacing: -0.5px; }
  .person { position: absolute; left: 40px; top: 108px; }
  .person-name { font-size: 17px; font-weight: 700; color: var(--brand); }
  .person-title { font-size: 12px; color: var(--ink); letter-spacing: 0.5px; margin-top: 2px; }
  .contact { position: absolute; left: 40px; top: 166px; list-style: none; }
  .contact li {
    display: flex; align-items: center; gap: 14px;
    font-size: 13px; color: var(--ink); line-height: 17px;
  }
  .contact li.web { color: var(--brand); }
  .contact-icon {
    width: 11px; height: 11px; border-radius: 50%;
    background: var(--brand); color: #fff;
    font-size: 7px; font-weight: 700; text-align: center; line-height: 11px;
  }
  .address { position: absolute; left: 40px; bottom: 28px; font-size: 12.5px; color: var(--ink); }
  .address strong { color: var(--brand); }
</style>
</head>
<body>
<main class="stage">
  <section class="card card-nfc">
    <div class="nfc-zone" role="img" aria-label="Soft NFC signal waves radiating around the brand mark, marking where to place the phone"></div>
    <p class="nfc-brand">netlinka</p>
    <p class="nfc-tagline">Aktiver NFC og legg mobilen din her!</p>
  </section>

  <section class="card card-contact">
    <div class="logo">
      <span class="logo-square"></span>
      <span class="logo-name">netlinka</span>
    </div>
    <div class="person">
      <p class="person-name">Erik Halvorsen</p>
      <p class="person-title">DIRECTOR</p>
    </div>
    <ul class="contact">
      <li><span class="contact-icon">t</span>+47 400 12 345</li>
      <li><span class="contact-icon">e</span>erik@netlinka.no</li>
      <li class="web"><span class="contact-icon">w</span>www.netlinka.no</li>
    </ul>
    <p class="address"><strong>Netlinka AS</strong>, Strandveien 12B, 1366 Lysaker</p>
  </section>
</main>
</body>
</html>
```